PWF - world groomers association website

Pacific Whisker Federation (PWF) is a new association located in USA, start the first project in South Korea. As now we do the following business:
1. We supply dog grooming education
2. We certify dog groomers
3. We host dog grooming education events
4. We organize grooming trade show

The design:
Because this organization is related to dog grooming, so beautiful groomed dog images are important. I will upload some well groomed dog images. I want you are able to put all these images or some of the images together either nice color or just layout of the images. I want the first page impressive. This business is related to grooming education, so I want our customers get impressed by visiting our website and decide to contact us for their continuing education. Also since this is an association, I want the website to be some level of institutional. Background layout and images catch eyes, but the content area simple and clear.

I want to be able to edit my site by adding images and edit the contents by myself in a easy way.

I need 5 pages now, but I may need to add more pages, but not more than 8 pages.

www.tollmarden.com is the site I really like.

Thanks.

• consistent tune on every page
• several well-groomed dogs, I can provide images

```html
<!DOCTYPE html>
<html lang="en">
<head>
<meta charset="utf-8">
<title>Our Certifiers – Pacific Whisker Federation</title>
<link href="https://fonts.googleapis.com/css2?family=Oswald:wght@400;500;700&family=Open+Sans:wght@400;600&display=swap" rel="stylesheet">
<style>
:root{
  --ink:#222;
  --muted:#666;
  --line:#d9d9d9;
  --navy:#1f3a6b;
  --green:#8cc63f;
  --lime:#a6cb4a;
  --gold:#c2a452;
  --crumb:#6d8fc2;
  --footer:#3b3b3b;
  --footer-line:#555;
  --footer-text:#e6e6e6;
  --topbar:#8fb0d8;
}
*{margin:0;padding:0;box-sizing:border-box}
html,body{width:806px;height:1200px;overflow:hidden;background:#fff}
body{position:relative;font-family:"Open Sans",Arial,sans-serif;color:var(--ink)}

.site-header{position:absolute;left:0;top:0;width:806px;height:54px;background:#fff;border-top:3px solid var(--topbar);z-index:2}
.brand{position:absolute;left:59px;top:3px;width:112px;height:112px;border-radius:50%;background:#fff;box-shadow:0 1px 4px rgba(0,0,0,.25);display:flex;align-items:center;justify-content:center;flex-direction:column;gap:5px;z-index:3}
.brand-dot{width:14px;height:14px;border-radius:50%;background:var(--navy)}
.brand-name{font-family:"Oswald",sans-serif;font-weight:500;font-size:20px;color:var(--navy);letter-spacing:1px}
.main-nav{position:absolute;left:183px;top:21px;display:flex;align-items:center}
.main-nav a{font-family:"Oswald",sans-serif;font-size:10.5px;color:var(--ink);text-decoration:none;margin-right:12px;white-space:nowrap}
.main-nav a.current{color:var(--gold)}

.hero{position:absolute;left:0;top:54px;width:806px;height:196px;background:linear-gradient(100deg,#dcd7d0 0%,#b7a692 30%,#8a7560 55%,#c8bfb4 75%,#5a4e44 100%)}
.hero-title{position:absolute;left:0;width:806px;top:72px;text-align:center;font-family:"Oswald",sans-serif;font-weight:700;font-size:45px;color:#fff;letter-spacing:1px;text-shadow:0 2px 4px rgba(0,0,0,.3)}
.hero-dots{position:absolute;left:364px;top:172px;display:flex;gap:4px}
.hero-dots span{width:17px;height:3px;background:#fff;border-radius:2px}
.hero-dots span.on{background:var(--lime)}

.breadcrumb{position:absolute;left:66px;top:268px;font-family:"Oswald",sans-serif;font-size:11px;color:var(--ink)}
.breadcrumb .sep{margin:0 4px;font-size:9px}
.breadcrumb .here{color:var(--crumb)}
.rule{position:absolute;left:66px;width:675px;height:1px;background:var(--line)}

.section-title{position:absolute;left:0;width:806px;top:316px;text-align:center;font-family:"Oswald",sans-serif;font-weight:500;font-size:16px;color:var(--ink)}
.section-intro{position:absolute;left:120px;width:566px;top:350px;text-align:center;font-size:8px;line-height:16px;color:var(--muted)}

.certifier{position:absolute;width:126px;text-align:center}
.certifier .photo{width:126px;height:129px;border:1px solid var(--line);padding:2px;background:#fff}
.certifier .photo div{width:100%;height:100%}
.certifier h3{font-family:"Oswald",sans-serif;font-weight:500;font-size:11.5px;margin-top:8px;color:var(--ink)}
.certifier p{font-size:9px;color:#888;margin-top:3px}

.partner{position:absolute;width:240px;text-align:center}
.partner .mark{height:96px;display:flex;align-items:center;justify-content:center;gap:8px;white-space:nowrap}
.partner .mark .dot{flex:none;width:14px;height:14px;border-radius:50%}
.partner .mark span{font-family:"Oswald",sans-serif;font-weight:500;font-size:17px}
.partner p{font-size:8px;line-height:16px;color:var(--muted);margin-top:16px}

.site-footer{position:absolute;left:0;top:994px;width:806px;height:206px;background:var(--footer);color:var(--footer-text)}
.site-footer h4{position:absolute;top:20px;font-family:"Oswald",sans-serif;font-weight:500;font-size:11px;color:#fff;letter-spacing:.3px}
.site-footer ul{position:absolute;top:45px;list-style:none}
.site-footer li{font-size:8px;line-height:13.8px}
.news-text{position:absolute;left:339px;top:45px;font-size:8px;line-height:12.5px;width:150px}
.news-input{position:absolute;left:339px;top:80px;width:181px;height:23px;background:#fff;font-size:7.5px;color:#666;padding:7px 9px}
.news-btn{position:absolute;left:339px;top:112px;width:63px;height:21px;background:var(--lime);color:#fff;font-family:"Oswald",sans-serif;font-size:8.5px;letter-spacing:.5px;text-align:center;line-height:21px}
.contact-row{position:absolute;left:572px;font-size:8px;line-height:10.5px;display:flex;gap:14px}
.contact-row svg{flex:none;margin-top:1px}
.footer-rule{position:absolute;left:66px;top:158px;width:675px;height:1px;background:var(--footer-line)}
.copyright{position:absolute;left:67px;top:175px;font-size:8px}
.social{position:absolute;left:644px;top:170px;display:flex;gap:3px}
.social span{width:22px;height:22px;border:1.5px solid #fff;border-radius:50%}
</style>
</head>
<body>

<header class="site-header">
  <nav class="main-nav">
    <a href="#">Home</a><a href="#">Event</a><a href="#">Our Partners</a><a href="#" class="current">Our Certifiers</a><a href="#">Grooming Education</a><a href="#">Grooming Product</a><a href="#">Contact Us</a><a href="#">Become Member</a><a href="#">Certifications</a>
    <svg width="9" height="9" viewBox="0 0 10 10" aria-label="Search"><circle cx="4" cy="4" r="3" fill="none" stroke="#222" stroke-width="1.6"/><line x1="6.2" y1="6.2" x2="9" y2="9" stroke="#222" stroke-width="1.8"/></svg>
  </nav>
</header>
<div class="brand"><span class="brand-dot"></span><span class="brand-name">PWF</span></div>

<section class="hero" role="img" aria-label="Groomer trimming a white dog's coat with scissors on a grooming table">
  <h1 class="hero-title">OUR CERTIFIERS</h1>
  <div class="hero-dots"><span class="on"></span><span></span><span></span><span></span></div>
</section>

<div class="breadcrumb">HOME <span class="sep">&gt;&gt;</span> <span class="here">OUR CERTIFIERS</span></div>
<div class="rule" style="top:290px"></div>

<h2 class="section-title">PWF/ TOLLMARDEN CERTIFICATION CERTIFIERS</h2>
<p class="section-intro">Nam libero tempore, cum soluta nobis est eligendi optio cumque nihil impedit quo minus id quod maxime placeat facere possimus, omnis voluptas assumenda est, omnis dolor repellendu autem quibusdam et aut officiis debitis aut rerum necessitatibuie</p>

<div class="certifier" style="left:66px;top:405px"><div class="photo"><div role="img" aria-label="Portrait of certifier Delia Marsh" style="background:linear-gradient(160deg,#e6e1dc,#b9a99a 60%,#3d2d28)"></div></div><h3>DELIA MARSH</h3><p>Florida</p></div>
<div class="certifier" style="left:203px;top:405px"><div class="photo"><div role="img" aria-label="Portrait of certifier Owen Pratt" style="background:linear-gradient(160deg,#f0f0ef,#c9c4be 55%,#5a5a5c)"></div></div><h3>OWEN PRATT</h3><p>Florida</p></div>
<div class="certifier" style="left:340px;top:405px"><div class="photo"><div role="img" aria-label="Portrait of certifier Nora Ellis" style="background:linear-gradient(160deg,#f2f2f2,#c7a892 55%,#4a2f24)"></div></div><h3>NORA ELLIS</h3><p>Florida</p></div>
<div class="certifier" style="left:477px;top:405px"><div class="photo"><div role="img" aria-label="Portrait of certifier Reid" style="background:linear-gradient(160deg,#d9dde2,#a9a6a4 50%,#2a2d36)"></div></div><h3>REID</h3><p>Florida</p></div>
<div class="certifier" style="left:614px;top:405px"><div class="photo"><div role="img" aria-label="Portrait of certifier Imani" style="background:linear-gradient(160deg,#8f9499,#8a5e40 50%,#e7e2df)"></div></div><h3>IMANI</h3><p>Florida</p></div>

<div class="certifier" style="left:66px;top:585px"><div class="photo"><div role="img" aria-label="Portrait of certifier Grant Cole" style="background:linear-gradient(160deg,#8e9c8a,#c9b8a8 45%,#2f3e63)"></div></div><h3>GRANT COLE</h3><p>Florida</p></div>
<div class="certifier" style="left:203px;top:585px"><div class="photo"><div role="img" aria-label="Portrait of certifier Vera" style="background:linear-gradient(160deg,#b98a5e,#9b6b4c 50%,#d9c7b5)"></div></div><h3>VERA</h3><p>Florida</p></div>
<div class="certifier" style="left:340px;top:585px"><div class="photo"><div role="img" aria-label="Portrait of certifier Tessa" style="background:linear-gradient(160deg,#f4f4f4,#c9a58f 50%,#2b2f3a)"></div></div><h3>TESSA</h3><p>Florida</p></div>
<div class="certifier" style="left:477px;top:585px"><div class="photo"><div role="img" aria-label="Portrait of certifier Delia Marsh" style="background:linear-gradient(160deg,#eef0f0,#c9a189 50%,#232838)"></div></div><h3>DELIA MARSH</h3><p>Florida</p></div>
<div class="certifier" style="left:614px;top:585px"><div class="photo"><div role="img" aria-label="Portrait of certifier Owen Pratt" style="background:linear-gradient(160deg,#d8c6ac,#6b4a36 50%,#1f2228)"></div></div><h3>OWEN PRATT</h3><p>Florida</p></div>

<div class="rule" style="top:784px"></div>

<div class="partner" style="left:111px;top:808px">
  <div class="mark"><span class="dot" style="background:var(--navy)"></span><span style="color:var(--navy)">Pacific Whisker Federation</span></div>
  <p>Nemo enim ipsam voluptatem quia voluptas sit aspernatur aut odit aut fugit, sed quia consequuntur magni dolores eos qui ratione voluptatem sequi nescio quisquam esrem</p>
</div>
<div class="partner" style="left:455px;top:808px">
  <div class="mark"><span class="dot" style="background:var(--green)"></span><span style="color:var(--green)">Tollmarden Productions, Inc.</span></div>
  <p>Nemo enim ipsam voluptatem quia voluptas sit aspernatur aut odit aut fugit, sed quia consequuntur magni dolores eos qui ratione voluptatem sequi nescio quisquam esrem</p>
</div>

<footer class="site-footer">
  <h4 style="left:66px">INFORMATION</h4>
  <ul style="left:66px"><li>Home</li><li>About</li><li>Education</li><li>Trade Shows</li><li>Certification</li><li>Events</li><li>Contact</li></ul>
  <h4 style="left:187px">QUICK LINKS</h4>
  <ul style="left:187px"><li>Membership Information</li><li>Membership Application</li><li>Find a Groomer</li><li>Member Directory</li><li>Groomer Training</li><li>Articles</li><li>Fundraising</li></ul>
  <h4 style="left:339px">NEWSLETTER SUBSCRIPTION</h4>
  <p class="news-text">Register your email Address to get information about us</p>
  <div class="news-input">Email Address</div>
  <div class="news-btn">SUBSCRIBE</div>
  <h4 style="left:572px">CONTACT US</h4>
  <div class="contact-row" style="top:48px"><svg width="7" height="9" viewBox="0 0 7 10" aria-label="Address"><path d="M3.5 0a3.5 3.5 0 0 0-3.5 3.5C0 6 3.5 10 3.5 10S7 6 7 3.5A3.5 3.5 0 0 0 3.5 0z" fill="#fff"/><circle cx="3.5" cy="3.5" r="1.3" fill="#3b3b3b"/></svg><span>48 Harbor Crest Lane, Suite 7,<br>97205, Portland</span></div>
  <div class="contact-row" style="top:80px"><svg width="9" height="9" viewBox="0 0 10 10" aria-label="Phone"><path d="M2 0l2 2.5-1 1.3a6 6 0 0 0 3.2 3.2l1.3-1L10 8l-1.5 2C4 9.5.5 6 0 1.5z" fill="#fff"/></svg><span>1 555 010 0199</span></div>
  <div class="contact-row" style="top:100px"><svg width="10" height="9" viewBox="0 0 10 9" aria-label="Fax"><rect x="0" y="2" width="10" height="7" fill="#fff"/><rect x="2" y="0" width="5" height="3" fill="#fff"/><rect x="2" y="4" width="2" height="1.4" fill="#3b3b3b"/><rect x="5" y="4" width="2" height="1.4" fill="#3b3b3b"/></svg><span>1 555 010 0142</span></div>
  <div class="contact-row" style="top:122px"><svg width="10" height="8" viewBox="0 0 10 8" aria-label="Email"><rect width="10" height="8" fill="#fff"/><path d="M0 0l5 4 5-4" fill="none" stroke="#3b3b3b" stroke-width="1"/></svg><span>info@pacificwhiskerfederation.com</span></div>
  <div class="footer-rule"></div>
  <p class="copyright">Copyrights © 2016, Pacific Whisker Federation. All Rights Reserved.</p>
  <div class="social"><span aria-label="Professional network"></span><span aria-label="Microblog"></span><span aria-label="Social network"></span><span aria-label="Photo sharing"></span></div>
</footer>

</body>
</html>
```